Gift Card Designs for different ocassions

We supply gift cards to retailers. Most use one design and we would like to offer them different card designs for different occasions. They would be Birthday, christmas, Fathers day, Mothers day. Others would be You Rock, You are a star, Thank You, Awesome stuff, My Hero, Great effort and congratulations.
We really want a fun, funky design that makes the gift card pop.

Target Market(s)

Anyone who buys a gift card

Colors

Designer to choose colors to be used in the design.

Requirements
Nice to have
• just need exciting , funky designs that stand out.
Should not have
• dull boring colours that make it look to corporate

```html
<!DOCTYPE html>
<html lang="en">
<head>
<meta charset="utf-8">
<title>Happy Birthday Gift Card</title>
<link rel="stylesheet" href="https://fonts.googleapis.com/css2?family=Dancing+Script:wght@700&display=swap">
<style>
  :root {
    --card-white: #f4f2f0;
    --cover-edge: #d9d6d3;
    --ink-cyan: #2fb8ee;
    --ink-blue: #5a86f0;
    --ink-violet: #9a5ef0;
    --ink-magenta: #d64fe0;
    --box-dark: #1e1e1f;
    --stick-wood: #e6d2b4;
    --head-teal: #2fa3b0;
    --head-purple: #8a4cc8;
    --head-lime: #b8c830;
    --head-red: #c0303a;
  }
  html, body {
    margin: 0;
    padding: 0;
    width: 1200px;
    height: 756px;
    overflow: hidden;
    background: var(--card-white);
  }
  .gift-card {
    position: relative;
    width: 1200px;
    height: 756px;
    overflow: hidden;
    background: var(--card-white);
  }
  .matchstick-area {
    position: absolute;
    top: 0;
    right: 0;
    width: 330px;
    height: 756px;
    background:
      linear-gradient(90deg, var(--stick-wood) 0%, #cdb696 45%, rgba(30,30,31,0) 60%),
      linear-gradient(180deg, var(--head-teal) 0%, var(--head-purple) 25%, var(--head-lime) 45%, var(--head-red) 60%, var(--head-purple) 78%, var(--head-teal) 100%),
      var(--box-dark);
    background-blend-mode: normal, multiply, normal;
  }
  .matchstick-area::after {
    content: "";
    position: absolute;
    top: 0;
    right: 0;
    width: 40px;
    height: 100%;
    background: var(--box-dark);
  }
  .cover {
    position: absolute;
    top: 0;
    left: 0;
    width: 880px;
    height: 756px;
    background: var(--card-white);
    box-shadow: 6px 0 14px rgba(0,0,0,0.35);
    border-right: 2px solid var(--cover-edge);
  }
  .greeting {
    position: absolute;
    left: 40px;
    top: 60px;
    width: 800px;
    margin: 0;
    font-family: "Dancing Script", cursive;
    font-weight: 700;
    text-align: center;
    line-height: 1;
    background: linear-gradient(100deg, var(--ink-cyan) 0%, var(--ink-blue) 30%, var(--ink-violet) 60%, var(--ink-magenta) 100%);
    -webkit-background-clip: text;
    background-clip: text;
    color: transparent;
  }
  .greeting-line {
    display: block;
  }
  .greeting-happy {
    font-size: 178px;
    margin-left: -30px;
  }
  .greeting-birthday {
    font-size: 178px;
    margin-top: -6px;
  }
  .greeting-to-you {
    font-size: 138px;
    margin-top: 14px;
    margin-left: -70px;
  }
</style>
</head>
<body>
  <main class="gift-card">
    <div class="matchstick-area" role="img" aria-label="Open matchbox with rows of wooden matches with colourful heads"></div>
    <section class="cover">
      <h1 class="greeting">
        <span class="greeting-line greeting-happy">Happy</span>
        <span class="greeting-line greeting-birthday">Birthday</span>
        <span class="greeting-line greeting-to-you">to You!</span>
      </h1>
    </section>
  </main>
</body>
</html>
```